Oil & Gas Service Brochure

We need to create a brochure that highlights the benefits of one of our services to oil and gas wells. We have a word document that includes a summary of the service and its problem solving benefits as well as some photos. The task will be to create a brochure using this information and our company logo and color schemes. Additionally, copy editing and proofing is preferred.

Target Market(s)

Oil & Gas Well Operators

```html
<!DOCTYPE html>
<html lang="en">
<head>
<meta charset="utf-8">
<title>Clear Path System – Service Brochure</title>
<link href="https://fonts.googleapis.com/css2?family=Saira+Semi+Condensed:wght@700;800&family=Saira:wght@700&family=Open+Sans:wght@400;600;700&display=swap" rel="stylesheet">
<style>
  :root{
    --brand-blue:#2b3a9e;
    --brand-blue-soft:#c9cde6;
    --ink:#1f2230;
    --text:#2c2f3a;
    --white:#ffffff;
    --canvas:#e2e4e8;
    --sheet:#f4f5f7;
    --green:#2e9a3a;
  }
  *{margin:0;padding:0;box-sizing:border-box}
  html,body{width:830px;height:1200px;overflow:hidden;background:var(--canvas)}
  .canvas{position:relative;width:830px;height:1200px;overflow:hidden;background:var(--canvas);
    font-family:"Open Sans",Arial,sans-serif;color:var(--text)}
  .spread-slot{position:absolute;top:345px;width:394px;height:510px;box-shadow:0 6px 18px rgba(0,0,0,.25)}
  .spread-slot.front{left:14px}
  .spread-slot.back{left:422px}
  .sheet{position:absolute;left:0;top:0;width:580px;height:750px;overflow:hidden;transform:scale(.68);transform-origin:0 0;
    background:linear-gradient(160deg,#fafbfc 0%,#eceef1 55%,#f6f7f8 100%)}

  /* shared */
  .section-heading{position:absolute;font-family:"Saira",Arial,sans-serif;font-weight:700;font-size:30px;letter-spacing:5px;
    color:var(--ink);text-transform:uppercase;line-height:1;border-left:3px solid var(--brand-blue);padding-left:11px}
  .site-url{position:absolute;top:724px;font-family:"Saira",Arial,sans-serif;font-weight:700;font-size:12px;letter-spacing:5.5px;
    color:var(--ink);text-transform:uppercase;white-space:nowrap}
  .site-url .accent{color:var(--brand-blue)}
  .url-rule{position:absolute;top:745px;height:5px;background:var(--brand-blue)}
  .num{position:absolute;width:20px;height:20px;border-radius:50%;background:var(--brand-blue);color:var(--white);
    font-weight:700;font-size:10px;display:flex;align-items:center;justify-content:center;box-shadow:0 0 0 2px var(--brand-blue-soft)}
  .item-text{position:absolute;font-size:7.8px;line-height:11.4px;text-align:justify;color:var(--text)}

  /* front page */
  .hero-photo{position:absolute;left:0;top:0;width:580px;height:268px;
    background:linear-gradient(180deg,#8fc0e8 0%,#cfe3f3 35%,#d9d6cf 55%,#d8322c 68%,#b9463c 80%,#c9c6bf 100%)}
  .title-panel{position:absolute;left:292px;top:177px;width:236px;height:210px;background:var(--brand-blue);
    padding:22px 8px 0 30px;color:var(--white);font-family:"Saira Semi Condensed",Arial,sans-serif;text-transform:uppercase;white-space:nowrap}
  .title-panel::before{content:"";position:absolute;left:20px;top:26px;width:2px;height:150px;background:var(--white)}
  .title-main{font-weight:800;font-size:25px;line-height:1.08}
  .title-sub{font-weight:700;font-size:17px;line-height:1.3;margin-top:6px}
  .title-corner{position:absolute;right:6px;bottom:6px}
  .photo-rule{position:absolute;left:52px;top:270px;width:217px;height:5px;background:var(--brand-blue)}
  .brand{position:absolute;left:54px;top:298px;display:flex;align-items:center;gap:10px}
  .brand-mark{width:52px;height:52px;border-radius:50%;background:var(--ink);flex:0 0 52px}
  .brand-name{font-family:"Saira Semi Condensed",Arial,sans-serif;font-weight:700;color:var(--brand-blue);font-size:16px;line-height:1.1;text-transform:uppercase;white-space:nowrap}
  .overview-heading{left:52px;top:392px}
  .overview-box{position:absolute;left:52px;top:430px;width:217px;height:267px;background:var(--brand-blue);color:var(--white);
    padding:30px 26px 0 28px;font-size:8.2px;line-height:11.6px;text-align:justify}

  /* back page */
  .summary-heading{left:52px;top:52px}
  .intro-box{position:absolute;left:52px;top:90px;width:243px;height:75px;background:var(--brand-blue);color:var(--white);
    padding:16px 14px 0 17px;font-weight:700;font-size:8.6px;line-height:14px}
  .intro-tail{position:absolute;left:258px;top:164px}
  .benefit-line{position:absolute;left:64px;top:192px;width:1px;height:190px;background:var(--brand-blue-soft)}
  .chart-frame{position:absolute;left:52px;width:243px;border:3px solid var(--brand-blue);background:var(--white)}
  .chart-frame.daily{top:430px;height:108px}
  .chart-frame.average{top:584px;height:94px}
  .chart-frame svg{display:block;width:100%;height:100%}
  .chart-caption{position:absolute;left:52px;width:243px;text-align:center;font-size:9px;color:var(--text)}
  .photo{position:absolute;left:334px;width:194px}
  .photo.one{top:52px;height:177px;background:linear-gradient(160deg,#8e8c86 0%,#5f5b55 45%,#a9a79f 100%)}
  .photo.two{top:252px;height:175px;background:linear-gradient(160deg,#8b8a84 0%,#c9b62c 45%,#6a665f 100%)}
  .photo.three{top:508px;height:176px;background:linear-gradient(160deg,#b5b3ad 0%,#6c6a4c 50%,#c2c0ba 100%)}
  .photo-tag{position:absolute;left:502px;width:16px;height:70px;background:var(--brand-blue);color:var(--white);
    font-weight:700;font-size:7px;display:flex;align-items:center;justify-content:center}
  .photo-tag span{transform:rotate(-90deg);white-space:nowrap}
  .photo-tag.one{top:47px}
  .photo-tag.two{top:252px}
  .photo-caption{position:absolute;left:334px;width:194px;font-size:6.8px;line-height:9.6px;text-align:justify;color:var(--text)}
  .photo-caption b{color:var(--brand-blue)}
</style>
</head>
<body>
<main class="canvas">

  <!-- front page -->
  <div class="spread-slot front">
    <section class="sheet">
      <div class="hero-photo" role="img" aria-label="Photo of red and yellow fire-water pipework and valves at an industrial oilfield site under a blue sky"></div>

      <div class="title-panel">
        <h1 class="title-main">Clear Path<br>System</h1>
        <p class="title-sub">For well<br>stimulation and<br>scale removal<br>services</p>
        <svg class="title-corner" width="16" height="16" viewBox="0 0 16 16"><polygon points="16,0 16,16 0,16" fill="#ffffff"/></svg>
      </div>

      <div class="photo-rule"></div>

      <div class="brand">
        <div class="brand-mark"></div>
        <div class="brand-name">Ridgeline<br>Well Solutions</div>
      </div>

      <h2 class="section-heading overview-heading">Overview</h2>

      <div class="overview-box">
        The origin of this service started in the DJ Basin when we discovered a need to increase production on older producing Plunger Lift wells. We found that after multiple rig workovers, the issue was not in the wellbore itself, but that the Perf or Slotted Sub had become either scaled or sanded off choking the well down to very little or no flow. Realizing the issue was fixable without doing an expensive traditional Workover, we purchased a device that allows us to perform basic ballistic procedures safely off our Slickline units. There are no other standard mechanical or hydraulic slickline perforating tools that can accomplish this service available. A typical job would look something like this.
      </div>

      <span class="num" style="left:288px;top:428px">1</span>
      <p class="item-text" style="left:320px;top:432px;width:208px">MIRU Slickline, RIH and pull plunger noting tight spots</p>
      <span class="num" style="left:288px;top:459px">2</span>
      <p class="item-text" style="left:320px;top:460px;width:208px">RIH and pull BSSV-note depth of nipple so we can correlate to tubing tally and wellbore diagram</p>
      <span class="num" style="left:288px;top:497px">3</span>
      <p class="item-text" style="left:320px;top:498px;width:208px">RIH with “dummy run” (Ardent Jars, Weight bars, Blind Box and Temperature Probe) drift through Profile Nipples to determine Perf Sub depth, establish bottom hole temperature and to locate fluid level.</p>
      <span class="num" style="left:288px;top:559px">4</span>
      <p class="item-text" style="left:320px;top:560px;width:208px">Once depths, fluid level and temperature have been confirmed and we know we are deep enough to get into the Perf Sub, RIHW Clear Path System® and either perforate new holes using a RTG (Retrievable Tubing Gun) or remove scale utilizing our Scale Clear®.</p>
      <span class="num" style="left:288px;top:634px">5</span>
      <p class="item-text" style="left:320px;top:634px;width:208px">Free flow well to determine if new or more communication has been established.</p>
      <span class="num" style="left:288px;top:673px">6</span>
      <p class="item-text" style="left:320px;top:673px;width:208px">RIHW broach to production nipple. Reset production tools and turn well back to the client</p>

      <div class="site-url" style="left:304px">www.<span class="accent">ridgelinefs</span>.com</div>
      <div class="url-rule" style="left:304px;width:224px"></div>
    </section>
  </div>

  <!-- summary page -->
  <div class="spread-slot back">
    <section class="sheet">
      <h2 class="section-heading summary-heading">Summary</h2>

      <div class="intro-box">This service can be done in a few hours if no unexpected well conditions are encountered. The main benefits are:</div>
      <svg class="intro-tail" width="16" height="9" viewBox="0 0 16 9"><polygon points="0,0 16,0 8,9" fill="#2b3a9e"/></svg>

      <div class="benefit-line"></div>
      <span class="num" style="left:55px;top:182px">1</span>
      <p class="item-text" style="left:87px;top:186px;width:209px">For a small investment, we can provide information on if the well needs to be worked over or not. IE if we perform this service and nothing changes, you know you have wellbore issues-NOT production tubing issues.</p>
      <span class="num" style="left:55px;top:250px">2</span>
      <p class="item-text" style="left:87px;top:253px;width:209px">This service is “greener” than a traditional workover by producing far less emissions. There is no need to kill the well or to flair any gas.</p>
      <span class="num" style="left:55px;top:293px">3</span>
      <p class="item-text" style="left:87px;top:297px;width:209px">When the service is successful, the data has shown an increase of 100%-600% in production! For example, we have stimulated wells that were making 2-3BBL/day before we performed this service, and they are now producing 50-70BBL/day!</p>
      <span class="num" style="left:55px;top:359px">4</span>
      <p class="item-text" style="left:87px;top:364px;width:209px">This service is cost effective enough that in most cases, the “free” increased production will pay for this service in 24-48 hours of running the well for 24-48 hours.</p>

      <div class="chart-frame daily">
        <svg viewBox="0 0 237 102" preserveAspectRatio="none" role="img" aria-label="Line chart of daily production before and after the Scale Clear service">
          <text x="118" y="10" text-anchor="middle" font-size="5" fill="#2b3a9e" font-family="Open Sans, sans-serif">Scale Clear: Case Well #001 - Production BPD</text>
          <line x1="22" y1="18" x2="22" y2="72" stroke="#9aa0b5" stroke-width=".6"/>
          <line x1="22" y1="72" x2="228" y2="72" stroke="#9aa0b5" stroke-width=".6"/>
          <g stroke="#e1e3ea" stroke-width=".4">
            <line x1="22" y1="27" x2="228" y2="27"/><line x1="22" y1="40" x2="228" y2="40"/><line x1="22" y1="53" x2="228" y2="53"/><line x1="22" y1="64" x2="228" y2="64"/>
          </g>
          <polyline fill="none" stroke="#4a6fc7" stroke-width="1" points="26,68 34,66 42,69 50,64 58,67 66,62 74,66 82,63 90,67 98,61 106,65 114,62 122,66 130,63 138,66 146,33 154,38 162,36 170,40 178,37 186,38 194,39 202,37 210,40 218,38 224,41"/>
          <g fill="#4a6fc7"><circle cx="146" cy="33" r="1"/><circle cx="26" cy="68" r="1"/><circle cx="224" cy="41" r="1"/></g>
          <text x="125" y="95" text-anchor="middle" font-size="4" fill="#2b3a9e" font-family="Open Sans, sans-serif">Date - Scale Clear Performed 5/18/2022</text>
        </svg>
      </div>
      <p class="chart-caption" style="top:546px">Daily Production Graph</p>

      <div class="chart-frame average">
        <svg viewBox="0 0 237 88" preserveAspectRatio="none" role="img" aria-label="Line chart comparing average daily production before and after the service">
          <text x="118" y="9" text-anchor="middle" font-size="4.5" fill="#2b3a9e" font-family="Open Sans, sans-serif">Average Daily Production Before / After Scale Clear Service - Case Well #001</text>
          <text x="118" y="16" text-anchor="middle" font-size="4.5" font-weight="700" fill="#2e9a3a" font-family="Open Sans, sans-serif">427% Increase in Production</text>
          <g stroke="#e1e3ea" stroke-width=".4">
            <line x1="14" y1="24" x2="218" y2="24"/><line x1="14" y1="38" x2="218" y2="38"/><line x1="14" y1="52" x2="218" y2="52"/><line x1="14" y1="66" x2="218" y2="66"/><line x1="14" y1="78" x2="218" y2="78"/>
          </g>
          <line x1="58" y1="66" x2="168" y2="46" stroke="#4a6fc7" stroke-width="1"/>
          <text x="58" y="85" text-anchor="middle" font-size="4" fill="#555" font-family="Open Sans, sans-serif">Before</text>
          <text x="168" y="85" text-anchor="middle" font-size="4" fill="#555" font-family="Open Sans, sans-serif">After</text>
        </svg>
      </div>
      <p class="chart-caption" style="top:686px">Average Daily Production</p>

      <div class="photo one" role="img" aria-label="Photo of a fully scaled perforated sub lying on a workover rig grating"></div>
      <div class="photo-tag one"><span>IMAGE 1</span></div>
      <div class="photo two" role="img" aria-label="Photo of the perforated sub painted yellow before the stimulation test"></div>
      <div class="photo-tag two"><span>IMAGE 2</span></div>
      <p class="photo-caption" style="top:438px"><b>Images 1-2:</b> Perforated Sub recovered from a Workover rig that was completely scaled off. I painted it yellow before the test to see how much scale came off when it was stimulated using our Scale Clear.</p>
      <div class="photo three" role="img" aria-label="Photo of the perforated sub after treatment with scale removed from its holes"></div>
      <p class="photo-caption" style="top:697px">Perforated Sub after utilizing Scale Clear. ALL scale removed from the sub opening the original 56 holes.</p>

      <div class="site-url" style="left:60px">www.<span class="accent">ridgelinefs</span>.com</div>
      <div class="url-rule" style="left:52px;width:243px"></div>
    </section>
  </div>

</main>
</body>
</html>
```